Online Rug Store needs Clearance Banner

Website is: Lanternfield Carpets and Home
You can access it at: www.lanternfieldcarpetsandhome.com and login (top right) with password: trazok

*** update: When creating banners for my site, you have permission to use images from www.velbora.com, but ONLY for this project. The images/artwork are copyright allowable for use on www.lanternfieldcarpetsandhome.com projects.***

We need a home page banner sized 1000 wide x 500 tall pixels to promote a "Clearance Sale" on rugs. The banner can state:

1. Clearance Sale
2. Now in progress
3. Save an extra 20% with coupon code 'Mint20'
4. Ends March 31st
5. Plus Free Shipping and 30 day returns.

We prefer a banner that appears hand-drawn and artistic, not commercially produced. It is OK to use a room scene image, rug images, or just a colored/textured background with text and no images. Your choice.

Flat graphics with no shadows and 3-D effect preferred.
Attached is are 3 logo options, as well as an example banner with handcrafted, artistic styling that we prefer.

Target Market(s)

This should be an eye-catching banner to showcase a very urgent promotion. Consider using colors of red, white, gold, and black to make a strong statement on the home page.

Industry/Entity Type

Home And Garden

Requirements
Must have
• Winner must provide Photoshop editable file format (.psd format) including layers that can be edited.
Nice to have
• Hand-drawn, stenciled, scribbled, artistic graphics and fonts is nice because we sell rugs that are made by hand.
Should not have
• little to no shadowing. Avoid computerized graphics.

```html
<!DOCTYPE html>
<html lang="en">
<head>
<meta charset="utf-8">
<title>Clearance Sale Banner</title>
<link href="https://fonts.googleapis.com/css2?family=Berkshire+Swash&family=Cinzel:wght@400;700&family=Luckiest+Guy&display=swap" rel="stylesheet">
<style>
  :root {
    --weave-light: #eeeae3;
    --weave-mid: #dcd6cb;
    --band-black: #0b0908;
    --sale-red: #8c1016;
    --coupon-gold: #f5d14a;
    --note-white: #f3efe6;
  }
  * { margin: 0; padding: 0; box-sizing: border-box; }
  html, body { width: 1200px; height: 600px; overflow: hidden; background: var(--weave-light); }
  .banner {
    position: relative;
    width: 1200px;
    height: 600px;
    background:
      repeating-linear-gradient(90deg, rgba(0,0,0,0.035) 0 2px, transparent 2px 7px),
      repeating-linear-gradient(0deg, rgba(0,0,0,0.03) 0 1px, transparent 1px 5px),
      var(--weave-light);
    overflow: hidden;
  }
  .rug-row { position: absolute; left: 0; width: 1200px; }
  .rug { position: absolute; display: block; }
  .rug-row--top { top: 20px; height: 140px; }
  .rug-row--bottom { top: 440px; height: 144px; }

  .headline {
    position: absolute;
    top: 182px;
    width: 100%;
    text-align: center;
    font-family: "Berkshire Swash", cursive;
    font-size: 90px;
    letter-spacing: 7px;
    color: var(--sale-red);
    line-height: 1;
  }
  .subhead {
    position: absolute;
    top: 278px;
    width: 100%;
    text-align: center;
    font-family: "Cinzel", serif;
    font-size: 36px;
    letter-spacing: 2px;
    color: var(--sale-red);
  }
  .offer-band {
    position: absolute;
    top: 336px;
    left: 0;
    width: 1200px;
    height: 98px;
    background: var(--band-black);
    text-align: center;
  }
  .coupon {
    padding-top: 13px;
    font-family: "Luckiest Guy", cursive;
    font-size: 40px;
    letter-spacing: 1px;
    color: var(--coupon-gold);
    line-height: 1.1;
  }
  .terms {
    margin-top: 6px;
    font-family: "Cinzel", serif;
    font-size: 21px;
    color: var(--note-white);
    letter-spacing: 0.5px;
  }
</style>
</head>
<body>
<main class="banner">
  <svg class="rug-row rug-row--top" width="1200" height="140" viewBox="0 0 1200 140">
    <rect class="rug" x="24" y="0" width="96" height="140" fill="#2a2624" role="img" aria-label="Black rug with circle pattern"/>
    <rect class="rug" x="144" y="0" width="96" height="140" fill="#a32a2a" role="img" aria-label="Red lattice rug"/>
    <rect class="rug" x="264" y="0" width="96" height="140" fill="#b44a36" role="img" aria-label="Rust bordered rug"/>
    <rect class="rug" x="384" y="0" width="96" height="140" fill="#d9cb7a" role="img" aria-label="Yellow geometric rug"/>
    <rect class="rug" x="492" y="0" width="120" height="140" fill="#9aa564" role="img" aria-label="Green floral rug"/>
    <rect class="rug" x="630" y="0" width="96" height="140" fill="#2a2624" role="img" aria-label="Black rug with circle pattern"/>
    <rect class="rug" x="744" y="0" width="96" height="140" fill="#5a5a5e" role="img" aria-label="Grey and blue floral rug"/>
    <rect class="rug" x="858" y="0" width="96" height="140" fill="#7fa0b4" role="img" aria-label="Blue rug with orange flower"/>
    <rect class="rug" x="972" y="0" width="96" height="140" fill="#4d8f6a" role="img" aria-label="Green and blue diamond rug"/>
    <rect class="rug" x="1086" y="0" width="96" height="140" fill="#c2cfa6" role="img" aria-label="Green chevron rug"/>
  </svg>

  <h1 class="headline">CLEARANCE SALE</h1>
  <p class="subhead">NOW IN PROGRESS</p>

  <section class="offer-band">
    <p class="coupon">SAVE AN EXTRA 20% WITH COUPON CODE 'MINT20'</p>
    <p class="terms">Ends March 31st. Free Shipping and 30 day returns.</p>
  </section>

  <svg class="rug-row rug-row--bottom" width="1200" height="144" viewBox="0 0 1200 144">
    <rect class="rug" x="0" y="0" width="86" height="144" fill="#8a6a2c" role="img" aria-label="Gold paisley rug"/>
    <rect class="rug" x="104" y="0" width="86" height="144" fill="#6e7478" role="img" aria-label="Grey medallion rug"/>
    <rect class="rug" x="210" y="0" width="86" height="144" fill="#c0661e" role="img" aria-label="Orange geometric rug"/>
    <rect class="rug" x="322" y="0" width="86" height="144" fill="#a59a80" role="img" aria-label="Beige patchwork rug"/>
    <rect class="rug" x="430" y="0" width="86" height="144" fill="#a9a6b8" role="img" aria-label="Multicolour check rug"/>
    <rect class="rug" x="556" y="0" width="100" height="144" fill="#8c8680" role="img" aria-label="Grey floral rug"/>
    <rect class="rug" x="672" y="0" width="86" height="144" fill="#ec7a62" role="img" aria-label="Red striped rug"/>
    <rect class="rug" x="782" y="0" width="86" height="144" fill="#5b6168" role="img" aria-label="Grey textured rug"/>
    <rect class="rug" x="892" y="0" width="100" height="144" fill="#c5d1a2" role="img" aria-label="Light green star rug"/>
    <rect class="rug" x="1022" y="0" width="90" height="144" fill="#8a3848" role="img" aria-label="Plum medallion rug"/>
    <rect class="rug" x="1136" y="0" width="64" height="144" fill="#7a5a34" role="img" aria-label="Brown floral rug"/>
  </svg>
</main>
</body>
</html>
```